Trust Icon Designs

We need 4 trust icons to display on our website. Our current ones need updating to better match our website. You can downlaod our current ones below and also view them here: https://www.corvelbangles.com.au/
The style is up to you but it needs to match the look and feel of our website.
Any questions, please ask!

Target Market(s)

Females 18-34

Industry/Entity Type

Jewelry

```html
<!DOCTYPE html>
<html lang="en">
<head>
<meta charset="utf-8">
<title>Corvel Bangles — Home</title>
<link rel="stylesheet" href="https://fonts.googleapis.com/css2?family=Open+Sans:ital,wght@0,300;0,400;0,600;0,700;1,400&family=Montserrat:wght@400;500&family=Quicksand:wght@500&display=swap">
<style>
:root{
  --blue:#2a7fc6;
  --link:#3d8fd1;
  --teal:#2f98bf;
  --plum:#8a3a8c;
  --ink:#333;
  --grey:#666;
  --soft:#999;
  --rule:#e2e2e2;
  --star:#f5b800;
  --silver:#e9e9ec;
}
*{box-sizing:border-box;margin:0;padding:0}
html,body{width:1200px;height:718px;overflow:hidden;background:#fff}
body{position:relative;font-family:"Open Sans",sans-serif;color:var(--ink)}
.abs{position:absolute}

/* header */
.brand{left:45px;top:6px;font-family:"Quicksand",sans-serif;font-weight:500;font-size:18px;line-height:19px;color:var(--blue)}
.section-ghost{left:0;width:1200px;top:-11px;text-align:center;font-family:"Montserrat",sans-serif;font-size:16px;color:#ddd;letter-spacing:1px}
.nav{left:480px;top:13px;display:flex;gap:11px;font-family:"Montserrat",sans-serif;font-size:11.5px;letter-spacing:1.1px;color:#444}
.nav .active{color:var(--blue)}
.nav .caret{display:inline-block;width:6px;height:6px;border-right:1px solid #777;border-bottom:1px solid #777;transform:rotate(45deg);margin-left:5px;position:relative;top:-3px}
.search{left:1153px;top:13px}
.cart-tab{left:1182px;top:0;width:18px;height:53px;background:var(--blue)}

/* products */
.product{top:70px;width:140px;text-align:center}
.product .shot{width:120px;height:128px;margin:0 auto;border-radius:6px;background:radial-gradient(circle at 50% 55%,#f4f4f6 0,#dcdce0 55%,#fff 80%)}
.product .name{margin-top:33px;font-weight:300;font-size:12px;line-height:17px;color:#555}
.product .price{margin-top:1px;font-size:11px;color:var(--link)}
.product .price i{font-style:italic}

/* trust tiles */
.trust{top:328px;width:124px;height:123px;color:#fff;text-align:center}
.trust.teal{background:linear-gradient(135deg,#35a3c9,#2a8db4)}
.trust.plum{background:linear-gradient(135deg,#94409a,#7d3382)}
.trust svg,.trust .mark{position:absolute;left:50%;top:18px;transform:translateX(-50%)}
.trust .label{position:absolute;left:0;right:0;top:79px;font-size:10.5px;font-weight:600;line-height:14px}
.trust .mark{width:56px;height:40px;border:2px solid #fff;border-radius:40% 50% 45% 55%}

/* reviews */
.reviews-title{left:160px;top:514px;font-size:16px;font-weight:600;color:#222}
.summary{left:871px;top:519px;display:flex;align-items:center;gap:6px;font-size:11px;color:#444}
.stars{color:var(--star);letter-spacing:1px}
.summary .stars{font-size:13px}
.arrows{left:1010px;top:513px;font-size:18px;color:#333;letter-spacing:10px}
.reviews-rule{left:160px;top:545px;width:905px;height:1px;background:var(--rule)}
.review{top:552px;width:283px}
.review .stars{font-size:20px;letter-spacing:2px}
.review .date{position:absolute;right:0;top:9px;font-size:8.5px;color:#888}
.review .title{margin-top:3px;font-size:14.5px;font-weight:600;color:#222}
.review .thumb{position:absolute;left:0;top:48px;width:61px;height:61px;border:1px solid #ddd;border-radius:3px;background:linear-gradient(#fafafa,#eceef0)}
.review .caption{position:absolute;left:0;top:118px;width:64px;font-size:7px;line-height:8px;color:#444}
.review .body{position:absolute;left:76px;top:48px;width:200px;font-style:italic;font-size:11px;line-height:13px;color:#777}
.review .who{margin-top:6px;font-style:normal;font-weight:600;font-size:9.5px;color:#555}
.review-edge{left:1064px;top:603px;width:1px;height:57px;background:#ddd}

.message{left:1098px;top:654px;width:99px;height:29px;border:1px solid #e5e5e5;border-radius:3px;background:#fff;display:flex;align-items:center;justify-content:center;gap:5px;font-size:11.5px;color:var(--blue)}
.message .dot{width:12px;height:12px;border-radius:50%;background:var(--blue)}
</style>
</head>
<body>

<div class="abs section-ghost">New Arrivals</div>
<div class="abs brand">Corvel<br>Bangles</div>

<nav class="abs nav">
  <span class="active">HOME</span>
  <span>SHOP<span class="caret"></span></span>
  <span>GIFT CARD</span>
  <span>SALE</span>
  <span>INSTASHOP</span>
  <span>GET $10 OFF</span>
</nav>
<svg class="abs search" width="12" height="12" viewBox="0 0 12 12" aria-label="Search"><circle cx="5" cy="5" r="4" fill="none" stroke="#666" stroke-width="1.2"/><line x1="8" y1="8" x2="11.5" y2="11.5" stroke="#666" stroke-width="1.2"/></svg>
<div class="abs cart-tab"></div>

<div class="abs product" style="left:168px"><div class="shot" role="img" aria-label="Silver necklace with four linked name hearts"></div><div class="name">Four Heart Name<br>Necklace</div><div class="price"><i>from</i> $69.99</div></div>
<div class="abs product" style="left:317px"><div class="shot" role="img" aria-label="Silver ring with baby feet and engraved date"></div><div class="name">Personalised Baby Feet<br>Ring</div><div class="price"><i>from</i> $44.99</div></div>
<div class="abs product" style="left:467px"><div class="shot" role="img" aria-label="Silver necklace with engraved heart charms"></div><div class="name">Heart Charm Necklace<br>- 3 To 5 Charms</div><div class="price"><i>from</i> $59.99</div></div>
<div class="abs product" style="left:616px"><div class="shot" role="img" aria-label="Silver family tree disc necklace with birthstones"></div><div class="name">Family Tree Disc<br>Necklace</div><div class="price"><i>from</i> $69.99</div></div>
<div class="abs product" style="left:766px"><div class="shot" role="img" aria-label="Silver heart and key necklace pair"></div><div class="name">Key To My Heart<br>Necklace Set</div><div class="price"><i>from</i> $59.99</div></div>
<div class="abs product" style="left:916px"><div class="shot" role="img" aria-label="Silver baby feet pendant necklace"></div><div class="name">Personalised Baby Feet<br>Necklace</div><div class="price"><i>from</i> $49.99</div></div>

<div class="abs trust teal" style="left:300px">
  <svg width="52" height="46" viewBox="0 0 52 46" fill="none" stroke="#fff" stroke-width="2.4" stroke-linejoin="round" stroke-linecap="round">
    <path d="M26 24 C12 14 16 3 24 6 C26 7 26 8 26 9 C27 4 36 3 37 10 C38 16 32 20 26 24Z"/>
    <path d="M4 30 L16 26 L30 28 C33 29 32 33 29 33 L20 33 M30 32 L44 24 C47 22 50 26 47 28 L30 40 L12 42 L6 44"/>
  </svg>
  <div class="label">Hand Made<br>With Love</div>
</div>
<div class="abs trust plum" style="left:465px">
  <div class="mark" role="img" aria-label="Outline map of Australia"></div>
  <div class="label">Owned &amp;<br>Operated</div>
</div>
<div class="abs trust teal" style="left:630px">
  <svg width="56" height="44" viewBox="0 0 56 44" fill="none" stroke="#fff" stroke-width="2.4" stroke-linejoin="round">
    <path d="M14 8 H50 V32 H6 V20 L14 8Z"/>
    <path d="M9 19 H18 V12 H14Z"/>
    <circle cx="15" cy="35" r="4.5" fill="#2f98bf"/>
    <circle cx="41" cy="35" r="4.5" fill="#2f98bf"/>
    <text x="35" y="24" fill="#fff" stroke="none" font-family="Open Sans,sans-serif" font-weight="700" font-size="11" text-anchor="middle">$30+</text>
  </svg>
  <div class="label">FREE Shipping<br>Worldwide</div>
</div>
<div class="abs trust plum" style="left:795px">
  <svg width="44" height="48" viewBox="0 0 44 48" fill="none" stroke="#fff" stroke-width="2.4" stroke-linejoin="round" stroke-linecap="round">
    <path d="M22 20 V6 C22 2 28 2 28 6 V20 H36 C39 20 40 22 40 25 V40 C40 43 38 45 35 45 H22 C18 45 16 43 16 40"/>
    <path d="M8 22 H20 C22 22 22 27 20 27 H8 C6 27 6 22 8 22Z M8 28 H20 C22 28 22 33 20 33 H8 C6 33 6 28 8 28Z M9 34 H19 C21 34 21 39 19 39 H9 C7 39 7 34 9 34Z"/>
  </svg>
  <div class="label">Happiness<br>Guaranteed</div>
</div>

<h2 class="abs reviews-title">Latest Reviews</h2>
<div class="abs summary"><span class="stars">★★★★★</span><span>275 Reviews</span></div>
<div class="abs arrows">&lt; &gt;</div>
<div class="abs reviews-rule"></div>

<article class="abs review" style="left:160px">
  <div class="stars">★★★★★</div><div class="date">28/08/2018</div>
  <div class="title">Love It</div>
  <div class="thumb" role="img" aria-label="Photo of heart charm necklace"></div>
  <div class="caption">Heart Charm Necklace - 3 To 5 Charms</div>
  <div class="body">I bought this item for a birthday gift and it is just perfect. Makes a really thoughtful present.<div class="who">Rosa M.</div></div>
</article>
<article class="abs review" style="left:459px">
  <div class="stars">★★★★★</div><div class="date">20/08/2018</div>
  <div class="title">good</div>
  <div class="thumb" role="img" aria-label="Photo of pet portrait pendant"></div>
  <div class="caption">My Furry Friend</div>
  <div class="body">really good really happy with it just as I expected it would be :)<div class="who">Jared T.</div></div>
</article>
<article class="abs review" style="left:757px">
  <div class="stars">★★★★★</div><div class="date">15/08/2018</div>
  <div class="title">Infinity</div>
  <div class="thumb" role="img" aria-label="Photo of infinity name necklace"></div>
  <div class="caption">Infinity Style Name Necklace</div>
  <div class="body">A gift for my daughter. She is a small woman who manages to accomplish amazing things and this was to let her know how much I love her.<div class="who">Paula K.</div></div>
</article>
<div class="abs review-edge"></div>

<div class="abs message"><span class="dot"></span>Message Us</div>

</body>
</html>
```